Offshore Energy Projects Management Consultancy needs a business card design

Logo available. We provide teams to deliver engineering consultancy, project management and delivery teams mainly in the offshore renewables sector. The company is all about bringing the right people to a project to deliver the scope.

The business card will be used for all staff.

The business card should be quite simple, vibrant and uncluttered but convey experience, enthusiasm and integration.

Target Market(s)

Energy Project Developers and Tier 1 construction companies

Contact Information for Business Card

Logo should be on the back of the card. I'm happy for the designer to play with the colour of the logo and background colour.

Front of the card should convey all the must have information in a clear and professional manner but without being overly traditional.

Colors

Designer to choose colors to be used in the design.

Requirements
Must have
• Land Line Tel Number, Mobile Tel Number, Email, business address, web address.

```html
<!DOCTYPE html>
<html lang="en">
<head>
<meta charset="utf-8">
<title>Seaward Delivery Group – Business Card</title>
<link href="https://fonts.googleapis.com/css2?family=Rubik:wght@400;500;700&display=swap" rel="stylesheet">
<style>
  :root {
    --backdrop: #2b2c2f;
    --blue-deep: #2c7ccd;
    --blue-bright: #4ab8e8;
    --accent: #2f86d6;
    --ink: #5b5d61;
    --ink-soft: #707276;
    --rule: #9a9ca0;
    --paper: #ffffff;
  }
  * { box-sizing: border-box; margin: 0; padding: 0; }
  html, body { width: 1200px; height: 1200px; overflow: hidden; }
  body {
    background: var(--backdrop);
    font-family: "Rubik", Arial, sans-serif;
    display: flex;
    flex-direction: column;
    align-items: center;
    justify-content: center;
    gap: 44px;
  }
  .card {
    width: 900px;
    height: 514px;
    border-radius: 26px;
    position: relative;
    overflow: hidden;
    box-shadow: 0 16px 36px rgba(0,0,0,.45);
  }
  /* Back */
  .card-back {
    background: linear-gradient(115deg, var(--blue-deep) 0%, #3a9ddc 55%, var(--blue-bright) 100%);
    display: flex;
    align-items: center;
    justify-content: center;
  }
  .brand {
    display: flex;
    align-items: center;
    gap: 16px;
    font-weight: 500;
    letter-spacing: .5px;
  }
  .brand-dot { width: 30px; height: 30px; border-radius: 50%; flex: none; }
  .card-back .brand { color: var(--paper); font-size: 44px; }
  .card-back .brand-dot { background: var(--paper); width: 38px; height: 38px; }

  /* Front */
  .card-front { background: var(--paper); display: flex; align-items: center; }
  .front-brand {
    width: 50%;
    display: flex;
    justify-content: center;
    padding-left: 30px;
  }
  .front-brand .brand { color: var(--accent); font-size: 30px; }
  .front-brand .brand-dot { background: var(--accent); }
  .divider {
    width: 2px;
    height: 290px;
    background: var(--rule);
    flex: none;
  }
  .contact {
    padding-left: 44px;
    color: var(--ink-soft);
  }
  .person-name { font-size: 34px; color: var(--ink); font-weight: 400; letter-spacing: 1px; }
  .person-name strong { font-weight: 700; }
  .person-role { font-size: 21px; color: var(--accent); letter-spacing: 1px; margin-top: 2px; margin-bottom: 24px; }
  .contact-list { list-style: none; }
  .contact-list li {
    display: flex;
    align-items: center;
    gap: 14px;
    font-size: 22px;
    line-height: 31px;
    letter-spacing: .8px;
  }
  .contact-list svg { width: 20px; height: 20px; fill: var(--accent); flex: none; }
  .address {
    font-style: normal;
    font-size: 22px;
    line-height: 28px;
    letter-spacing: .8px;
    margin-top: 24px;
  }
</style>
</head>
<body>
  <section class="card card-back" aria-label="Card back">
    <div class="brand"><span class="brand-dot"></span>Seaward Delivery Group</div>
  </section>

  <section class="card card-front" aria-label="Card front">
    <div class="front-brand">
      <div class="brand"><span class="brand-dot"></span>Seaward Delivery Group</div>
    </div>
    <div class="divider"></div>
    <div class="contact">
      <h1 class="person-name"><strong>Marcus</strong> Ellery</h1>
      <p class="person-role">CEO/Founder</p>
      <ul class="contact-list">
        <li>
          <svg viewBox="0 0 24 24" aria-hidden="true"><path d="M6.6 10.8a15.1 15.1 0 0 0 6.6 6.6l2.2-2.2c.3-.3.7-.4 1-.2 1.1.4 2.3.6 3.6.6.6 0 1 .4 1 1V20c0 .6-.4 1-1 1A17 17 0 0 1 3 4c0-.6.4-1 1-1h3.5c.6 0 1 .4 1 1 0 1.3.2 2.5.6 3.6.1.3 0 .7-.2 1z"/></svg>
          214 555 0187
        </li>
        <li>
          <svg viewBox="0 0 24 24" aria-hidden="true"><path d="M6 2h12v5H6zM3 8h18a1 1 0 0 1 1 1v8h-4v5H6v-5H2V9a1 1 0 0 1 1-1zm5 8v4h8v-4z"/></svg>
          214 555 0188
        </li>
        <li>
          <svg viewBox="0 0 24 24" aria-hidden="true"><path d="M2 5h20v14H2zm2 2v.5l8 5.5 8-5.5V7l-8 5.3z"/></svg>
          marcus@seawarddelivery.com
        </li>
        <li>
          <svg viewBox="0 0 24 24" aria-hidden="true"><path d="M12 2a10 10 0 1 0 0 20 10 10 0 0 0 0-20zm6.9 6h-3a15 15 0 0 0-1.3-3.9A8 8 0 0 1 18.9 8zM12 4c.8 1.1 1.5 2.5 1.9 4h-3.8c.4-1.5 1.1-2.9 1.9-4zM4.3 14a8 8 0 0 1 0-4h3.4a16 16 0 0 0 0 4zm.8 2h3a15 15 0 0 0 1.3 3.9A8 8 0 0 1 5.1 16zm3-8h-3a8 8 0 0 1 4.3-3.9A15 15 0 0 0 8.1 8zM12 20c-.8-1.1-1.5-2.5-1.9-4h3.8c-.4 1.5-1.1 2.9-1.9 4zm2.3-6H9.7a14 14 0 0 1 0-4h4.6a14 14 0 0 1 0 4zm.3 5.9a15 15 0 0 0 1.3-3.9h3a8 8 0 0 1-4.3 3.9zm1.7-5.9a16 16 0 0 0 0-4h3.4a8 8 0 0 1 0 4z"/></svg>
          www.seawarddelivery.com
        </li>
      </ul>
      <address class="address">48 Quayside Road<br>Suite 300, Bayport<br>MI 49000</address>
    </div>
  </section>
</body>
</html>
```